Business Card Design

I design and sell kitchens. I would like the card to have a black background either gloss or matt and a stripe through the middle in deep sky blue, the same blue as the team ridgeway pro cycling team. Written in the blue stripe in white i would like Harbourline kitchens in italics. underneath the stripe, again in white i would like 'the complete design and installation service. On the reverse i would like the following in simple black on white
Owen Tramley
07814 296540
email- owentramley@harbourlinekitchens-example.co.uk
Web- WWW.harbourlinekitchens-example.co.uk

I have added a copy of an initial idea for a logo but it can be changed to suit the brief above

Industry/Entity Type

Business

Contact Information for Business Card

Harbourline Kitchens
The complete design and installation service
Owen Tramley
07814 296540-mob
owentramley@harbourlinekitchen-example.co.uk
WWW.harbourlinekitchens-example.co.uk

```html
<!DOCTYPE html>
<html lang="en">
<head>
<meta charset="utf-8">
<title>Harbourline Kitchens – Business Card</title>
<link rel="stylesheet" href="https://fonts.googleapis.com/css2?family=Open+Sans:ital,wght@0,300;0,400;0,700;1,400&display=swap">
<style>
  :root {
    --sky-blue: #12a9df;
    --card-black: #0c0c0d;
    --card-white: #ffffff;
    --ink: #111111;
    --tagline: #e6e6e6;
    --backdrop: #e9e7e3;
  }
  * { box-sizing: border-box; margin: 0; padding: 0; }
  html, body {
    width: 1200px; height: 1023px; overflow: hidden;
    background: var(--backdrop);
    font-family: "Open Sans", Arial, sans-serif;
  }
  .stage { position: relative; width: 1200px; height: 1023px; }

  .card {
    position: absolute;
    box-shadow: 0 10px 28px rgba(0,0,0,.28);
  }

  /* Front side */
  .card-front {
    left: 140px; top: 80px; width: 660px; height: 370px;
    background: linear-gradient(160deg, #1c1c1e 0%, var(--card-black) 45%, #050505 100%);
  }
  .card-front .stripe {
    position: absolute; left: 0; right: 0; top: 112px; height: 140px;
    background: var(--sky-blue);
    display: flex; align-items: center; justify-content: center;
  }
  .brand-name {
    font-weight: 700; line-height: 1.02; letter-spacing: -0.5px;
  }
  .card-front .brand-name { color: #ffffff; font-size: 50px; }
  .card-front .tagline {
    position: absolute; right: 46px; bottom: 36px;
    color: var(--tagline); font-weight: 300; font-size: 23px; letter-spacing: 0.3px;
  }

  /* Reverse side */
  .card-back {
    left: 300px; top: 480px; width: 680px; height: 410px;
    background: var(--card-white);
  }
  .card-back .brand-name {
    position: absolute; right: 60px; top: 36px;
    color: var(--sky-blue); font-size: 46px; text-align: left;
  }
  .contact {
    position: absolute; left: 40px; bottom: 30px;
  }
  .contact-name {
    color: var(--sky-blue); font-style: italic; font-size: 24px; margin-bottom: 6px;
  }
  .contact-line {
    display: flex; align-items: center; gap: 7px;
    color: var(--ink); font-style: italic; font-size: 18px; line-height: 27px;
  }
  .contact-line svg { width: 18px; height: 18px; flex: none; }
</style>
</head>
<body>
<main class="stage">

  <section class="card card-front" aria-label="Business card front">
    <div class="stripe">
      <div class="brand-name">Harbourline<br>Kitchens</div>
    </div>
    <p class="tagline">The complete design and installation service</p>
  </section>

  <section class="card card-back" aria-label="Business card reverse">
    <div class="brand-name">Harbourline<br>Kitchens</div>

    <div class="contact">
      <p class="contact-name">Owen Tramley</p>

      <p class="contact-line">
        <svg viewBox="0 0 18 18" aria-hidden="true">
          <circle cx="9" cy="9" r="9" fill="var(--sky-blue)"/>
          <rect x="6" y="3.5" width="6" height="11" rx="1.2" fill="none" stroke="#fff" stroke-width="1.3"/>
          <circle cx="9" cy="12.4" r="0.8" fill="#fff"/>
        </svg>
        07814 296540
      </p>

      <p class="contact-line">
        <svg viewBox="0 0 18 18" aria-hidden="true">
          <circle cx="9" cy="9" r="9" fill="var(--sky-blue)"/>
          <rect x="4" y="5.5" width="10" height="7" fill="none" stroke="#fff" stroke-width="1.2"/>
          <path d="M4 5.5 L9 9.6 L14 5.5" fill="none" stroke="#fff" stroke-width="1.2"/>
        </svg>
        owentramley@harbourlinekitchens-example.co.uk
      </p>

      <p class="contact-line">
        <svg viewBox="0 0 18 18" aria-hidden="true">
          <circle cx="9" cy="9" r="9" fill="var(--sky-blue)"/>
          <circle cx="9" cy="9" r="5" fill="none" stroke="#fff" stroke-width="1.1"/>
          <ellipse cx="9" cy="9" rx="2.2" ry="5" fill="none" stroke="#fff" stroke-width="1"/>
          <path d="M4 9 H14 M5 6.5 H13 M5 11.5 H13" stroke="#fff" stroke-width="0.9"/>
        </svg>
        www.harbourlinekitchens-example.co.uk
      </p>
    </div>
  </section>

</main>
</body>
</html>
```